Website design for online service business

The company provides the following services:
1 - consultancy services on existing products (like teamvault and deskline 354)
2 - Coaching services - Coach someone on services like using/developing features with existing products, or teach how to be more productive, or improve their business using automation, etc
3 - Training
- Online training on demand on existing products via voxora (like in Teamvault and deskline 365)
- Online courses through videos lessons and scripts by offering information products where people will need to register and pay in advance to access the online course. (productivity courses for example)

- The goal is for clients to book time with me for one of those areas without too many clicks.
- Clients will be able to Book time using an integration (it would be good to have the layout integrated with the site.) with this https://planner.brellix.example/cal/BrightPathWorks1@brightpathworks.brellix.example/slots/

- there will be areas for which i whish to build a VIP mailing list. It's referenced on the wireframes

References:
https://www.ledgerandlanternhub.example/about/about-dorvin/
https://www.quillandcompass.example/
https://teamvaultsage.example/

Target Market(s)

- Small businesses
- Freelancers

Industry/Entity Type

Business

Number of Pages Required

5+ page

Font styles to use
Sans Serif

Colors

Designer to choose colors to be used in the design.

Requirements
Must have
• Must have the design optimized to the less clicks possible to achieve any action
• The colors of the site should follow the logo (provided in attach)
• It should use other color that belong to the same pallet of colors
• Should contain colors that incentivizes people to click and book something
• Images and backgrounds should be made available
• All images sizes and colors should be provided to be able to develop the site according to the design
Nice to have
• The bookings for the time should be integrated within the design. If not possible a redirection to it can work as well.
Should not have
• Links to social media
• Pop-ups
• Intrusive navigations (like navigation bares on the left or right hand side)
• Should not be a template used by many people

```html
<!DOCTYPE html>
<html lang="en">
<head>
<meta charset="utf-8">
<title>Bright Path Works – Digital Consultant</title>
<link rel="stylesheet" href="https://fonts.googleapis.com/css2?family=Montserrat:wght@500;600;700&family=Open+Sans:wght@400;600;700&display=swap">
<style>
  :root {
    --ink: #333333;
    --body: #555555;
    --brand-blue: #1b6fa8;
    --accent-orange: #f0a020;
    --band-grey: #ececec;
    --white: #ffffff;
    --footer: #3f4245;
    --footer-text: #8a8d90;
  }
  * { box-sizing: border-box; margin: 0; padding: 0; }
  html, body { width: 765px; height: 1200px; overflow: hidden; }
  body {
    position: relative;
    background: var(--white);
    font-family: "Open Sans", Arial, sans-serif;
    color: var(--body);
  }
  .heading { font-family: "Montserrat", Arial, sans-serif; color: var(--ink); font-weight: 600; }

  /* Header */
  .site-header {
    position: absolute; left: 0; top: 0; width: 765px; height: 56px;
    border-bottom: 1px solid #e6e6e6; background: var(--white);
  }
  .brand {
    position: absolute; left: 80px; top: 17px;
    display: flex; align-items: center; gap: 6px;
    font-family: "Open Sans", Arial, sans-serif; font-weight: 700;
    font-size: 12px; letter-spacing: 0.5px; color: var(--brand-blue);
  }
  .brand-mark { width: 12px; height: 12px; background: var(--brand-blue); }
  .main-nav { position: absolute; right: 68px; top: 20px; display: flex; gap: 13px; }
  .main-nav a { font-size: 10.5px; color: var(--brand-blue); text-decoration: none; }

  /* Divider */
  .divider { display: flex; align-items: center; gap: 5px; }
  .divider .line { width: 38px; height: 1.5px; background: var(--accent-orange); }
  .divider svg { width: 18px; height: 13px; }
  .centered > .divider { justify-content: center; margin-top: 6px; }

  /* Hero */
  .hero { position: absolute; left: 0; top: 57px; width: 765px; height: 234px; }
  .hero-text { position: absolute; left: 64px; top: 24px; width: 300px; }
  .hero-title { font-size: 19px; letter-spacing: 0.3px; }
  .hero-text .divider { margin-top: 6px; }
  .hero-sub { font-size: 10.5px; margin-top: 12px; }
  .hero-list { list-style: none; margin-top: 12px; font-size: 8.5px; line-height: 15.7px; color: var(--body); }
  .hero-photo {
    position: absolute; left: 391px; top: 27px; width: 311px; height: 184px;
    background: linear-gradient(135deg, #5f6b55 0%, #8a8f86 45%, #b9b2a8 70%, #6d6f72 100%);
  }

  /* Section: work so far */
  .work-band {
    position: absolute; left: 0; top: 291px; width: 765px; height: 224px;
    background: var(--band-grey);
  }
  .section-title { font-size: 17.5px; text-align: center; }
  .work-band .section-title { margin-top: 50px; }
  .work-copy {
    width: 640px; margin: 18px auto 0; text-align: center;
    font-size: 7.9px; line-height: 16px;
  }

  /* Testimonials */
  .testimonials { position: absolute; left: 0; top: 515px; width: 765px; height: 423px; }
  .testimonials .section-title { margin-top: 47px; }
  .testimonial { font-size: 7.8px; line-height: 15.7px; }
  .quote { position: absolute; }
  .avatar {
    position: absolute; width: 92px; height: 80px;
    background: linear-gradient(180deg, #c9d6e6 0%, #2d7fd0 100%);
    border-radius: 4px;
  }
  .t1 .avatar { left: 64px; top: 99px; }
  .t1 .quote { left: 174px; top: 100px; width: 530px; }
  .t2 .avatar { left: 609px; top: 191px; }
  .t2 .quote { left: 64px; top: 191px; width: 532px; }
  .t3 .avatar { left: 64px; top: 281px; }
  .t3 .quote { left: 174px; top: 282px; width: 530px; }

  /* Call to action */
  .cta {
    position: absolute; left: 0; top: 938px; width: 765px; height: 225px;
    background: linear-gradient(120deg, #4a3b33 0%, #2f3338 35%, #5a4240 60%, #2c3e55 100%);
    text-align: center; color: var(--white);
  }
  .cta .section-title { color: var(--white); font-weight: 700; margin-top: 49px; font-size: 18.5px; }
  .cta-copy { font-size: 8.5px; margin-top: 17px; line-height: 12px; }
  .cta-copy + .cta-copy { margin-top: 9px; }
  .cta-button {
    display: inline-block; margin-top: 14px; width: 74px; height: 20px; line-height: 20px;
    background: var(--brand-blue); color: var(--white); font-size: 8px; font-weight: 700;
    text-decoration: none; letter-spacing: 0.3px;
  }

  /* Footer */
  .site-footer {
    position: absolute; left: 0; top: 1163px; width: 765px; height: 37px;
    background: var(--footer); font-size: 7.5px; color: var(--footer-text);
  }
  .site-footer .copyright { position: absolute; left: 64px; top: 15px; }
  .site-footer .to-top { position: absolute; right: 64px; top: 15px; color: var(--brand-blue); text-decoration: none; }
</style>
</head>
<body>

<header class="site-header">
  <div class="brand"><span class="brand-mark"></span>BRIGHT PATH WORKS</div>
  <nav class="main-nav">
    <a href="#">Service</a>
    <a href="#">Blog</a>
  </nav>
</header>

<section class="hero">
  <div class="hero-text">
    <h1 class="hero-title heading">Hi , I´m Tobias</h1>
    <div class="divider">
      <span class="line"></span>
      <svg viewBox="0 0 18 13" aria-hidden="true"><path d="M1 2 L8.5 3.5 L8.5 12 L1 10.5 Z M17 2 L9.5 3.5 L9.5 12 L17 10.5 Z" fill="#1b6fa8"/></svg>
      <span class="line"></span>
    </div>
    <h2 class="hero-sub heading">A digital consultant that can help you with:</h2>
    <ul class="hero-list">
      <li>products like Teamvault, Deskline365</li>
      <li>or</li>
      <li>help you with your design and branding</li>
      <li>or</li>
      <li>bring your business into the online world</li>
      <li>or even</li>
      <li>help you create an online information product</li>
    </ul>
  </div>
  <div class="hero-photo" role="img" aria-label="Portrait photo of the consultant on a tree-lined street"></div>
</section>

<section class="work-band centered">
  <h2 class="section-title heading">What I have done so far</h2>
  <div class="divider">
    <span class="line"></span>
    <svg viewBox="0 0 18 13" aria-hidden="true"><path d="M1 2 L8.5 3.5 L8.5 12 L1 10.5 Z M17 2 L9.5 3.5 L9.5 12 L17 10.5 Z" fill="#1b6fa8"/></svg>
    <span class="line"></span>
  </div>
  <p class="work-copy">Lorem ipsum dolor sit amet, consectetur adipiscing elit. Quis enim redargueret? Ita prorsus, inquam; Longum est enim ad omnia respondere, quae a te dicta sunt. Qua ex cognitione facilior facta est investigatio rerum occultissimarum. Non enim ipsa genuit hominem, sed accepit a natura inchoatum. Duo Reges: constructio interrete. Quis suae urbis conservatorem Codrum, quis Erechthei filias non maxime laudat? Magni enim aestimabat pecuniam non modo non contra leges, sed etiam legibus partam. Dicet pro me ipsa virtus nec dubitabit isti vestro beato M.</p>
</section>

<section class="testimonials centered">
  <h2 class="section-title heading">What others say about me</h2>
  <div class="divider">
    <span class="line"></span>
    <svg viewBox="0 0 18 13" aria-hidden="true"><path d="M1 2 L8.5 3.5 L8.5 12 L1 10.5 Z M17 2 L9.5 3.5 L9.5 12 L17 10.5 Z" fill="#1b6fa8"/></svg>
    <span class="line"></span>
  </div>

  <div class="testimonial t1">
    <div class="avatar" role="img" aria-label="Client avatar illustration"></div>
    <p class="quote">Lorem ipsum dolor sit amet, consectetur adipiscing elit. Quis enim redargueret? Ita prorsus, inquam; Longum est enim ad omnia respondere, quae a te dicta sunt. Qua ex cognitione facilior facta est investigatio rerum occultissimarum. Non enim ipsa genuit hominem, sed accepit a natura inchoatum. Duo Reges: constructio interrete. Quis suae urbis conservatorem Codrum, quis Erechthei filias non maxime laudat? Magni enim aestimabat pecuniam non modo non contra leges, sed etiam legibus partam. Dicet pro me ipsa virtus nec dubitabit isti vestro beato M.Lorem ipsum dolor sit amet, consectetur adipiscing elit. Quis enim redargueret? Ita prorsus, inquam; Longum est</p>
  </div>

  <div class="testimonial t2">
    <p class="quote">Lorem ipsum dolor sit amet, consectetur adipiscing elit. Quis enim redargueret? Ita prorsus, inquam; Longum est enim ad omnia respondere, quae a te dicta sunt. Qua ex cognitione facilior facta est investigatio rerum occultissimarum. Non enim ipsa genuit hominem, sed accepit a natura inchoatum. Duo Reges: constructio interrete. Quis suae urbis conservatorem Codrum, quis Erechthei filias non maxime laudat? Magni enim aestimabat pecuniam non modo non contra leges, sed etiam legibus partam. Dicet pro me ipsa virtus nec dubitabit isti vestro beato M.Lorem ipsum dolor sit amet, consectetur adipiscing elit. Quis enim redargueret? Ita prorsus, inquam; Longum est</p>
    <div class="avatar" role="img" aria-label="Client avatar illustration"></div>
  </div>

  <div class="testimonial t3">
    <div class="avatar" role="img" aria-label="Client avatar illustration"></div>
    <p class="quote">Lorem ipsum dolor sit amet, consectetur adipiscing elit. Quis enim redargueret? Ita prorsus, inquam; Longum est enim ad omnia respondere, quae a te dicta sunt. Qua ex cognitione facilior facta est investigatio rerum occultissimarum. Non enim ipsa genuit hominem, sed accepit a natura inchoatum. Duo Reges: constructio interrete. Quis suae urbis conservatorem Codrum, quis Erechthei filias non maxime laudat? Magni enim aestimabat pecuniam non modo non contra leges, sed etiam legibus partam. Dicet pro me ipsa virtus nec dubitabit isti vestro beato M.Lorem ipsum dolor sit amet, consectetur adipiscing elit. Quis enim redargueret? Ita prorsus, inquam; Longum est</p>
  </div>
</section>

<section class="cta centered" role="img" aria-label="Darkened background photo of people studying together">
  <h2 class="section-title heading">Do you have any questions?</h2>
  <div class="divider">
    <span class="line"></span>
    <svg viewBox="0 0 18 13" aria-hidden="true"><path d="M1 2 L8.5 3.5 L8.5 12 L1 10.5 Z M17 2 L9.5 3.5 L9.5 12 L17 10.5 Z" fill="#1b6fa8"/></svg>
    <span class="line"></span>
  </div>
  <p class="cta-copy">Use the button bellow to book a time slot where we can have a chat about what you need help with and we will take it from there.</p>
  <p class="cta-copy">With coffee included of course!</p>
  <a class="cta-button" href="https://planner.brellix.example/cal/BrightPathWorks1@brightpathworks.brellix.example/slots/">TALK TO ME</a>
</section>

<footer class="site-footer">
  <span class="copyright">Copyright Bright Path Works 2018</span>
  <a class="to-top" href="#">Top</a>
</footer>

</body>
</html>
```